Cigarette Packaging for a luxury smoking brand

I need to do a new packaging for my cigarette brand new flavor and i need you to provide me with the source files and also with renders with 3d mockups. The design must include the cigarette box for 20 cigs, the outer box that contains 10 package of 20 cigs each, and the cigarrette must also be designed using black paper. I will provide our logo and other information that's required. The new flavor is called "Orvin". You can see our other product designs at www.vorela-pack.uk but the layout you can freely change it as long the design contains the name "VORELA" and the logo symbol, and the flavor name "Orvin"
Updates

Dear Designers. Thank you very much for your work.
Sadly i was unaware that the www.vorela-pack.uk website was attacked by a malware and that the page was offline. I apologize for that. The issue is solved now and the page is back on. I like some of the designs seen, but sadly the designs are too focused on the logo and not on the stylish or luxury concept. I suggest you have a look on how we use the logo on the existing designs on vorela-pack.uk and find a way to make a unique design based on your creativity. Please feel free to message me if you have any question or suggestion and i will be happy to assist. Focus more on the name and flavor and a smaller logo somewhere in the package and not big logo.

Target Market(s)

Tobacco consumers

Industry/Entity Type

tobacco

Colors

Designer to choose only greyscale colors for use in the design.

Requirements
Must have
• My name and logo, name can be any color but logo is usually on debossed or embossed with gold foil
Nice to have
• i would prefer a dark or black packaging
Should not have
• pink nor girly colors,

```html
<!DOCTYPE html>
<html lang="en">
<head>
<meta charset="utf-8">
<title>VORELA Orvin – Pack Artwork</title>
<link rel="stylesheet" href="https://fonts.googleapis.com/css2?family=Cinzel:wght@500&family=Oranienbaum&display=swap">
<style>
  :root {
    --canvas: #ffffff;
    --panel: #231f20;
    --gold: #d9a92c;
    --gold-light: #f6e27a;
    --gold-deep: #a8741a;
    --bronze: #b9772f;
    --frame: #a77a2a;
  }
  * { margin: 0; padding: 0; box-sizing: border-box; }
  html, body {
    width: 1200px; height: 1162px; overflow: hidden;
    background: var(--canvas);
  }
  .artboard { position: relative; width: 1200px; height: 1162px; }

  .pack-face {
    position: absolute;
    background: var(--panel);
    overflow: hidden;
  }
  .pack-face--front { left: 78px; top: 96px; width: 402px; height: 569px; }
  .pack-face--carton { left: 46px; top: 772px; width: 1108px; height: 353px; }

  .frame-outer, .frame-inner {
    position: absolute;
    border: 1px solid var(--frame);
  }
  .frame-outer { inset: 8px; }
  .frame-inner { inset: 12px; }
  .frame-dot {
    position: absolute; width: 4px; height: 4px;
    border: 1px solid var(--frame); border-radius: 50%;
  }

  .ornament {
    position: absolute;
    border-radius: 45% 55% 40% 60%;
    background: radial-gradient(ellipse at 50% 50%, rgba(217,169,44,0.55), rgba(168,116,26,0.18) 60%, rgba(35,31,32,0) 75%);
  }

  .brand-block {
    position: absolute; left: 0; right: 0;
    display: flex; flex-direction: column; align-items: center;
  }
  .brand-mark {
    width: 30px; height: 30px; border-radius: 50%;
    background: var(--gold);
  }
  .brand-name {
    font-family: "Cinzel", serif;
    font-weight: 500;
    color: var(--bronze);
    line-height: 1;
  }
  .rule {
    height: 2px;
    background: linear-gradient(90deg, rgba(217,169,44,0), var(--gold-light) 50%, rgba(217,169,44,0));
  }
  .flavor-name {
    font-family: "Oranienbaum", serif;
    line-height: 0.8;
    background: linear-gradient(90deg, var(--gold-deep), var(--gold-light) 45%, var(--gold) 70%, var(--gold-deep));
    -webkit-background-clip: text; background-clip: text;
    color: transparent;
    letter-spacing: 2px;
  }
  .tagline {
    font-family: "Cinzel", serif;
    color: var(--gold);
    letter-spacing: 1.5px;
  }

  /* front face sizing */
  .pack-face--front .brand-block { top: 122px; }
  .pack-face--front .brand-mark { width: 34px; height: 34px; margin-bottom: 40px; }
  .pack-face--front .brand-name { font-size: 38px; }
  .pack-face--front .rule { width: 348px; margin: 6px 0 12px; }
  .pack-face--front .flavor-name { font-size: 136px; }
  .pack-face--front .rule--lower { margin: 10px 0 12px; }
  .pack-face--front .tagline { font-size: 14px; }

  /* carton face sizing */
  .pack-face--carton .brand-block { top: 38px; }
  .pack-face--carton .brand-mark { width: 32px; height: 32px; margin-bottom: 38px; }
  .pack-face--carton .brand-name { font-size: 34px; }
  .pack-face--carton .rule { width: 304px; margin: 7px 0 10px; }
  .pack-face--carton .flavor-name { font-size: 138px; }
  .pack-face--carton .rule--lower { margin: 10px 0 12px; }
  .pack-face--carton .tagline { font-size: 13px; }
</style>
</head>
<body>
<main class="artboard">

  <section class="pack-face pack-face--front" aria-label="Pack front">
    <div class="frame-outer"></div>
    <div class="frame-inner"></div>
    <span class="frame-dot" style="left:6px;top:6px"></span>
    <span class="frame-dot" style="right:6px;top:6px"></span>
    <span class="frame-dot" style="left:6px;bottom:6px"></span>
    <span class="frame-dot" style="right:6px;bottom:6px"></span>

    <div class="ornament" role="img" aria-label="Gold line-art tobacco leaves with flourishes, top right corner" style="left:222px;top:11px;width:174px;height:162px"></div>
    <div class="ornament" role="img" aria-label="Gold line-art tobacco leaves with flourishes, bottom left corner" style="left:14px;top:381px;width:159px;height:181px"></div>

    <div class="brand-block">
      <span class="brand-mark"></span>
      <span class="brand-name">VORELA</span>
      <span class="rule"></span>
      <span class="flavor-name">ORVIN</span>
      <span class="rule rule--lower"></span>
      <span class="tagline">PREMIUM CIGARETTE</span>
    </div>
  </section>

  <section class="pack-face pack-face--carton" aria-label="Carton face">
    <div class="frame-outer"></div>
    <div class="frame-inner"></div>
    <span class="frame-dot" style="left:6px;top:6px"></span>
    <span class="frame-dot" style="right:6px;top:6px"></span>
    <span class="frame-dot" style="left:6px;bottom:6px"></span>
    <span class="frame-dot" style="right:6px;bottom:6px"></span>

    <div class="ornament" role="img" aria-label="Gold line-art tobacco leaves with flourishes, top left corner" style="left:21px;top:18px;width:144px;height:131px"></div>
    <div class="ornament" role="img" aria-label="Gold line-art tobacco leaves with flourishes, bottom right corner" style="left:955px;top:201px;width:140px;height:138px"></div>

    <div class="brand-block">
      <span class="brand-mark"></span>
      <span class="brand-name">VORELA</span>
      <span class="rule"></span>
      <span class="flavor-name">ORVIN</span>
      <span class="rule rule--lower"></span>
      <span class="tagline">PREMIUM CIGARETTE</span>
    </div>
  </section>

</main>
</body>
</html>
```